Clark County Assessor Canditate

We need a billboard ad for a political candidate Tessa Harrow who is running for Clark County Assessor in an upcoming election. Needs to be simple and to the point to get the people to see the name "Tessa Harrow" and what to vote for "Clark County Assessor" in Las Vegas, NV. Also the billboard visibility is best in the top side of the sign, so the information should be most prominent in the top right, middle, left sides.The size of the billboard is 14 ft Height X 48 ft Wide Also needs some bright colors that are noticable from a freeway viewed billboard.Designers - I need to have "Paid for by Tessa Harrow for Clark County Assessor" on the sign
I have uploaded a few headshots you can work with to create a design. Thank you,

http://tessaharrow-vote.info/

Voters

Political

• Name, what I am voting for, and some image that represents Las Vegas and/or Nevada

```html
<!DOCTYPE html>
<html lang="en">
<head>
<meta charset="utf-8">
<title>Tessa Harrow for Clark County Assessor – Billboard</title>
<link rel="stylesheet" href="https://fonts.googleapis.com/css2?family=Alegreya+Sans:wght@700;800&family=PT+Sans:wght@700&family=PT+Sans+Narrow:wght@700&family=Belleza&display=swap">
<style>
  :root {
    --civic-blue: #2b4b9b;
    --board-white: #ffffff;
    --frame-grey: #4a4d52;
    --page-bg: #eef1f5;
    --hair-light: #e3c790;
    --hair-mid: #c9a466;
    --jacket: #2c2a2e;
  }
  * { margin: 0; padding: 0; box-sizing: border-box; }
  html, body {
    width: 1200px;
    height: 598px;
    overflow: hidden;
    background: var(--page-bg);
  }
  .billboard {
    position: absolute;
    left: 30px;
    top: 140px;
    width: 1140px;
    height: 325px;
    background: var(--board-white);
    border: 3px solid var(--frame-grey);
  }
  .slogan-band {
    position: absolute;
    left: 0;
    right: 10px;
    top: 172px;
    height: 58px;
    background: var(--civic-blue);
  }
  .slogan-rule {
    position: absolute;
    left: 0;
    right: 10px;
    top: 238px;
    height: 3px;
    background: var(--civic-blue);
  }
  .civic-seal {
    position: absolute;
    left: 27px;
    top: 20px;
    width: 238px;
    height: 238px;
  }
  .civic-seal-name {
    font-family: "PT Sans", sans-serif;
    font-weight: 700;
    font-size: 15px;
    letter-spacing: 1px;
    fill: var(--board-white);
  }
  .candidate-photo {
    position: absolute;
    left: 169px;
    top: -44px;
    width: 340px;
    height: 366px;
    border-radius: 150px 150px 0 0;
    background: linear-gradient(180deg, var(--hair-light) 0%, var(--hair-mid) 55%, var(--jacket) 88%);
  }
  .headline {
    position: absolute;
    left: 520px;
    right: 20px;
    text-align: center;
    color: var(--civic-blue);
  }
  .office-title {
    top: 26px;
    font-family: "PT Sans Narrow", sans-serif;
    font-weight: 700;
    font-size: 33px;
    line-height: 1;
  }
  .candidate-name {
    top: 64px;
    font-family: "Alegreya Sans", sans-serif;
    font-weight: 800;
    font-size: 80px;
    line-height: 1;
  }
  .slogan {
    position: absolute;
    left: 520px;
    right: 20px;
    top: 180px;
    text-align: center;
    font-family: "Belleza", sans-serif;
    font-size: 36px;
    line-height: 1.1;
    color: var(--board-white);
  }
  .location {
    position: absolute;
    left: 520px;
    right: 20px;
    top: 258px;
    text-align: center;
    font-family: "PT Sans", sans-serif;
    font-weight: 700;
    font-size: 28px;
    letter-spacing: 2px;
    line-height: 1;
    color: var(--civic-blue);
  }
  .disclaimer {
    position: absolute;
    right: 18px;
    bottom: 6px;
    font-family: "PT Sans", sans-serif;
    font-weight: 700;
    font-size: 12px;
    line-height: 1;
    color: var(--civic-blue);
    white-space: nowrap;
  }
</style>
</head>
<body>
  <main class="billboard">
    <div class="slogan-band"></div>
    <div class="slogan-rule"></div>

    <svg class="civic-seal" viewBox="0 0 238 238" aria-label="City of Mesa Vista">
      <circle cx="119" cy="119" r="117" fill="var(--civic-blue)"/>
      <text class="civic-seal-name" x="72" y="112" text-anchor="middle">CITY OF</text>
      <text class="civic-seal-name" x="72" y="134" text-anchor="middle">MESA VISTA</text>
    </svg>

    <div class="candidate-photo" role="img" aria-label="Headshot of candidate Tessa Harrow, smiling, with long blonde hair and a dark blazer"></div>

    <p class="headline office-title">Clark County Assessor</p>
    <h1 class="headline candidate-name">Tessa Harrow</h1>
    <p class="slogan">“Working for You”</p>
    <p class="location">LAS VEGAS • NEVADA</p>
    <p class="disclaimer">Paid for by Tessa Harrow for Clark County Assessor</p>
  </main>
</body>
</html>
```